Webdesign Kornbach 31
Zielgruppe
Beratung zu Treppenliften
Aufgabenstellung
Im Wesentlichen wird das Layout für die Startseite gesucht (Landingpage).
Inhaltsseiten sollten aber gedanklich berücksichtigt werden.
Die Detailierte Beschreibung finden Sie in den PDF der Anlagen.
Bitte unbedingt diese Dokumente beachten!
--- Allgemein
Ich (der Auftraggeber) bin Betreiber einer kleinen Webseiten-Agentur und suche nach neuen Wegen um an umsetzbare und ansprechende und dennoch individuell auf den Kunden abgestimmte Layoutvorschläge zu kommen.
Die Programmierung wird auf jeden Fall von mir durchgeführt.

```html
<!DOCTYPE html>
<html lang="de">
<head>
<meta charset="utf-8">
<title>Kornbach 31 – Treppenlift Beratung</title>
<link href="https://fonts.googleapis.com/css2?family=Fira+Sans:wght@500;600;700&family=Open+Sans:wght@400;600;700&display=swap" rel="stylesheet">
<style>
:root{
  --blue:#0a5bab;
  --title:#2c6fb3;
  --pale:#bddcf3;
  --mist:#e9edf2;
  --field:#e3e9f1;
  --text:#3a3a3a;
  --muted:#6b6b6b;
  --line:#cfd6df;
}
*{box-sizing:border-box;margin:0;padding:0}
html,body{width:1200px;height:4439px;overflow:hidden}
body{position:relative;background:#fff;font-family:"Open Sans",sans-serif;color:var(--text)}
.abs{position:absolute}
.bg{position:absolute;left:0;top:0;width:1200px;height:4439px;z-index:0}
.layer{position:relative;z-index:1}
.topbar{font-size:11px;color:var(--muted);z-index:3}
.brand{left:88px;top:82px;display:flex;align-items:center;gap:10px;font-family:"Fira Sans",sans-serif;font-weight:600;font-size:18px;color:var(--blue)}
.brand i{width:22px;height:22px;border-radius:50%;background:var(--blue);display:block}
.nav{top:100px;font-size:12px;color:#555;z-index:3}
.btn{display:inline-flex;align-items:center;justify-content:center;background:var(--blue);color:#fff;border-radius:20px;font-size:12px;font-weight:600;z-index:3}
.diamond{position:absolute;transform:rotate(45deg);border-radius:60px;overflow:hidden}
h1{font-family:"Fira Sans",sans-serif;font-weight:600;font-size:26px;line-height:34px;color:#4a4a4a}
.sec-title{left:0;width:1200px;text-align:center;font-family:"Fira Sans",sans-serif;font-weight:600;font-size:21px;color:var(--title)}
.sec-sub{left:0;width:1200px;text-align:center;font-size:14px;color:var(--text)}
.card{background:#fff;box-shadow:0 3px 14px rgba(0,0,0,.12);border-radius:6px}
.field{background:var(--field);font-size:11px;color:#666;padding:0 14px;display:flex;align-items:center}
.check{width:32px;height:32px;background:var(--field)}
.small{font-size:13px;color:var(--text)}
.small b{color:var(--blue)}
.feat h2{font-family:"Fira Sans",sans-serif;font-weight:600;font-size:25px;color:#3a3a3a}
.feat .bar{width:52px;height:5px;background:var(--blue);border-radius:3px;margin:12px 0 14px}
.feat p{font-size:14.5px;line-height:25.7px;color:#4a4a4a}
.faq{left:88px;width:1024px;border:1.5px solid var(--line);border-radius:6px;background:#fff;display:flex;align-items:center;font-size:17px;color:var(--title)}
.faq span{width:58px;text-align:center;font-size:24px;color:#888;font-weight:300}
.answer{left:88px;width:1024px;border:1.5px solid var(--line);border-radius:6px;background:#fff;padding:26px 16px;font-size:14px;line-height:20px}
.answer b{color:#333}.answer b.l{color:var(--blue)}
.review{background:#fff;text-align:center;padding:22px 32px}
.review .stars{color:var(--blue);font-size:15px;letter-spacing:3px}
.review p{font-size:11px;font-style:italic;line-height:16px;color:#555;margin-top:12px}
.review .av{width:30px;height:30px;border-radius:50%;background:#c9a99a;margin:12px auto 6px}
.review .n{font-size:11px;font-weight:700;color:var(--blue)}
.review .c{font-size:9px;color:#777}
.maker{top:4140px;font-family:"Fira Sans",sans-serif;font-weight:600;font-size:26px;color:#1d4f8c;display:flex;align-items:center;gap:8px}
.maker i{display:block;width:22px;height:22px;background:#1d4f8c}
.foot{top:4305px;left:88px;font-size:10px;color:#666;display:flex;gap:10px}
</style>
</head>
<body>
<svg class="bg" viewBox="0 0 1200 4439" aria-hidden="true">
  <polygon points="0,855 371,517 647,790 0,1680" fill="#e9edf2"/>
  <polygon points="0,1680 647,790 720,870 0,1300" fill="#e9edf2" opacity=".5"/>
  <polygon points="1200,1775 1200,2600 1050,2600 560,2600" fill="#bddcf3"/>
  <polygon points="0,3900 340,3560 560,3560 0,4130" fill="#e9edf2"/>
</svg>

<div class="layer">
  <div class="diamond" role="img" aria-label="Foto: gepolsterter blauer Treppenliftsitz an einer Holztreppe mit Gehstock" style="left:578px;top:-60px;width:520px;height:520px;background:linear-gradient(135deg,#ded4c8,#b9a58e 45%,#3f6f96)"></div>

  <div class="abs topbar" style="left:100px;top:20px">☏ Telefon: 0800 555013-1</div>
  <div class="abs topbar" style="left:990px;top:20px;color:#333">◑ Kontrast umstellen</div>
  <div class="abs brand"><i></i>Kornbach 31</div>
  <div class="abs nav" style="left:800px">Startseite ⌄</div>
  <div class="abs nav" style="left:898px">● DE</div>
  <div class="abs btn" style="left:1022px;top:95px;width:90px;height:25px">Kontakt</div>

  <h1 class="abs" style="left:88px;top:324px">Bleiben Sie mobil mit einem<br>Treppenlift für Ihr Haus<br>oder Ihre Wohnung.</h1>
  <div class="abs" style="left:88px;top:440px;font-size:13px;color:#666">Wir möchten das Sie mobil in Ihren 4 Wänden bleiben</div>
  <div class="abs btn" style="left:88px;top:494px;width:123px;height:26px">Treppenlift planen</div>

  <div class="abs sec-title" style="top:702px">An welchem Ort soll der Lift montiert werden?</div>
  <div class="abs sec-sub" style="top:740px">Wer soll das Angebot erhalten?</div>

  <div class="abs card" style="left:88px;top:798px;width:1024px;height:374px">
    <div class="abs check" style="left:17px;top:34px"></div><div class="abs small" style="left:64px;top:44px;font-size:11px">Frau</div>
    <div class="abs check" style="left:125px;top:34px"></div><div class="abs small" style="left:172px;top:44px;font-size:11px">Herr</div>
    <div class="abs field" style="left:17px;top:98px;width:490px;height:37px">Name*</div>
    <div class="abs field" style="left:517px;top:98px;width:490px;height:37px">Vorname</div>
    <div class="abs field" style="left:17px;top:157px;width:490px;height:37px">Telefonnummer</div>
    <div class="abs field" style="left:517px;top:157px;width:490px;height:37px">Email-Adresse*</div>
    <div class="abs small" style="left:17px;top:213px;font-size:13.5px">Mit dem absenden meiner Anfrage akzeptiere ich die <b>AGB</b> und, dass ich die <b>Datenschutzerklärung</b> zur Kenntnis genommen habe.</div>
    <div class="abs btn" style="left:22px;top:264px;width:983px;height:43px;flex-direction:column;font-weight:400;font-size:15px;line-height:16px">Angebot erhalten<span style="font-size:10px">kostenlos &amp; unverbindlich</span></div>
    <div class="abs small" style="left:17px;top:335px;font-size:13.5px">Wir können Ihnen Informationen über ähnliche Produkte und Leistungen per E-Mail zusenden. Ein Widerspruch ist jederzeit <b>hier</b> möglich.</div>
  </div>

  <div class="abs feat" style="left:118px;top:1332px;width:455px">
    <h2>Kurvenlift</h2><div class="bar"></div>
    <p>Kurvenlifte unterscheiden mehr oder weniger nur hinsichtlich der Schienen von Treppenliften für gerade Treppen. Aufgrund der zahlreichen individuellen Treppenformen, müssen die Schienensysteme von Kurventreppenliften in der Regel maßgefertigt werden. Sowohl Sitzlifte als auch Plattformlifte sind als Kurventreppenlift erhältlich.</p>
  </div>
  <div class="abs btn" style="left:118px;top:1577px;width:124px;height:27px">Mehr erfahren</div>
  <div class="diamond" style="left:676px;top:1334px;width:300px;height:300px;background:#ececec"></div>
  <div class="diamond" role="img" aria-label="Foto: Kurventreppenlift mit braunem Sitz an weißer Treppe" style="left:652px;top:1336px;width:300px;height:300px;background:linear-gradient(135deg,#f5f5f3,#d8d4cf 55%,#6e4b3a)"></div>

  <div class="diamond" style="left:148px;top:1740px;width:300px;height:300px;background:var(--pale)"></div>
  <div class="diamond" role="img" aria-label="Foto: weißer Außentreppenlift an einer Außentreppe im Grünen" style="left:176px;top:1736px;width:300px;height:300px;background:linear-gradient(135deg,#5d8a3f,#e9e9e9 45%,#9b9b9b)"></div>
  <div class="abs feat" style="left:622px;top:1737px;width:455px">
    <h2>Außenlift</h2><div class="bar"></div>
    <p>Der Einsatz eines Treppenlifts im Außenbereich stellt erhöhte Anforderungen an das Material. Entsprechende Modell verfügen über verzinkte Fahrgestelle, eine versiegelte Antriebselektronik sowie Führungsschienen aus rostfreiem Aluminium. Während bei Sitzliften und klassischen Plattformliften zwischen Innen- und Außenlift unterschieden wird, sind fast alle Hublifte von vornherein für den Außenbereich geeignet.</p>
  </div>
  <div class="abs btn" style="left:622px;top:2000px;width:124px;height:27px">Mehr erfahren</div>

  <div class="abs feat" style="left:118px;top:2153px;width:455px">
    <h2>Gerader Treppenlift</h2><div class="bar"></div>
    <p>Gerade Treppenlifte bzw. Treppenlifte für gerade Treppen sind deutlich preiswerter als Treppenlifte für Kurventreppen (z. B. L-Form oder U-Form). Grund sind die Führungsschienen, die bei einem geraden Treppenverlauf nicht individuell maßgefertigt werden müssen.</p>
  </div>
  <div class="abs btn" style="left:118px;top:2364px;width:124px;height:27px">Mehr erfahren</div>
  <div class="diamond" style="left:676px;top:2157px;width:300px;height:300px;background:#fff"></div>
  <div class="diamond" role="img" aria-label="Foto: gerader Treppenlift an einer Holztreppe im Flur" style="left:652px;top:2160px;width:300px;height:300px;background:linear-gradient(135deg,#ece8e2,#c9bba8 50%,#3d2b22)"></div>

  <div class="abs sec-title" style="top:2579px">Wichtige Fragen zum Treppenlift</div>
  <div class="abs faq" style="top:2639px;height:59px"><span>+</span>Was sollte ich beim Kauf eines Treppenlifts beachten?</div>
  <div class="abs faq" style="top:2712px;height:58px"><span>+</span>Brauchen Rollstuhlfahrer speziell angepasste Treppenlifte?</div>
  <div class="abs faq" style="top:2784px;height:57px"><span>–</span>Werden Treppenlifte bezuschusst?</div>
  <div class="abs answer" style="top:2857px;height:112px">Falls ein <b>Pflegegrad</b> vorliegt, <b class="l">beteiligt sich die Krankenkasse</b> bzw. Pflegeversicherung an der Anschaffung eines Treppenlifts. Arbeitgeber werden bei der Einrichtung <b>behindertengerechter Arbeitsplätze</b> z. B. vom <b>Integrationsamt</b> unterstützt. Eine <b class="l">Förderung durch die Förderbank</b> ist ebenfalls möglich.</div>
  <div class="abs faq" style="top:2983px;height:56px"><span>+</span>Gibt es spezielle Treppenlifte für außen?</div>

  <div class="abs sec-title" style="top:3105px;font-size:18px">Kundenmeinungen</div>
  <div class="abs sec-sub" style="top:3141px">Unsere Zusammenarbeit beruht auf Vertrauen</div>
  <div class="abs" role="img" aria-label="Foto: Treppe mit Treppenlift und blauem Sitz" style="left:0;top:3191px;width:1200px;height:357px;background:linear-gradient(90deg,#e8e6e3,#d9d5d0 50%,#c8ccd2 80%,#5f86ad)"></div>
  <div class="abs review" style="left:234px;top:3253px;width:335px;height:255px">
    <div class="stars">★★★★★</div>
    <p>"Wir waren auf der Suche nach einem passenden Treppenlift für meine Schwiegermutter. Dank Pflegegrad haben wir einen Zuschuss von der Pflegekasse erhalten. Wir möchten uns für die umfangreiche Beratung und den schnellen Einbau bedanken."</p>
    <div class="av"></div><div class="n">Helga M.</div><div class="c">Connewitz</div>
  </div>
  <div class="abs review" style="left:629px;top:3253px;width:335px;height:255px">
    <div class="stars">★★★★★</div>
    <p>"Für einen langjährigen Mitarbeiter, der nach einem schweren Unfall im Rollstuhl sitzt, brauchten wir eine schnelle Lösung. Für uns war der Hublift die perfekte Wahl. Danke für die Beratung und die schnelle Umsetzung."</p>
    <div class="av"></div><div class="n">Rainer K.</div><div class="c">Potsdam</div>
  </div>

  <div class="abs sec-title" style="top:3612px;font-size:18px">Haben Sie Fragen, dann kontaktieren Sie uns gerne.</div>
  <div class="abs card" style="left:88px;top:3679px;width:1024px;height:329px">
    <div class="abs field" style="left:17px;top:29px;width:490px;height:38px">Name</div>
    <div class="abs field" style="left:517px;top:29px;width:490px;height:38px">E-Mailadresse</div>
    <div class="abs field" style="left:17px;top:88px;width:990px;height:150px;align-items:flex-start;padding-top:16px">Ihre Nachricht</div>
    <div class="abs check" style="left:17px;top:274px;width:22px;height:22px"></div>
    <div class="abs small" style="left:53px;top:277px">Ich habe den <b>Datenschutz</b> gelesen und verstanden.</div>
    <div class="abs btn" style="left:517px;top:262px;width:488px;height:38px;font-weight:400">Jetzt kostenlos beraten lassen</div>
  </div>

  <div class="abs sec-title" style="top:4058px;font-size:18px">Anbieter &amp; Hersteller</div>
  <div class="abs maker" style="left:106px">Stufenwerk</div>
  <div class="abs maker" style="left:305px">Stegora <i></i></div>
  <div class="abs maker" style="left:518px">Nordhang</div>
  <div class="abs maker" style="left:730px;font-weight:500;font-size:22px;color:#2c6fb3"><i style="border-radius:50%;background:#2c6fb3"></i>Hebeland</div>
  <div class="abs maker" style="left:962px;font-size:20px">Alpina Motion</div>

  <div class="abs" style="left:88px;top:4286px;width:1024px;height:1px;background:#bbb"></div>
  <div class="abs foot"><span>Impressum</span><span>Rechtliche Hinweise</span><span>Datenschutz</span><span>Cookie-Einstellungen</span><span>Sicherheit und Technik</span></div>
  <div class="abs btn" style="left:996px;top:4298px;width:116px;height:25px;font-weight:400">↑ Nach oben</div>
</div>
</body>
</html>
```